Modern & Simple Essential Oils Label

Company Name: Meadowlark Essentials

What we sell: Aromatherapy products, pure therapeutic essential oils.

Design need:
We are looking for a creative and youthful design for the labels used on small essentials oils.

I have two sizes of bottles that I use for essential oils a 5ml bottle and a 15ml bottle. They are dark Amber color glass with black lids. I like the clear labels or mayble a dark brown background. With white or clear lettering with punch of color too! Each oil type is represented by different color. (lavender- purple, lemon - yellow). The label will be the same for all the oils in the two sizes with only a different oil name & coordinating color.
5ml label size should be: 1 " x 2.625"
15ml label size should be: 1.5" x 3.5"

I have some labels that I have had another designer start on, but they aren't quite what I want and missing that something (alot!).. I don't know what. Interest maybe? Lack of design? I dunno.. they are attached. Maybe it's the logo? I don't know! But its gotta change! When I cut out a proof and put a sample on the bottle as I look straight on at the label all I see is a big dot, no logo.. nothing interesting.
Updates

Project Deadline Extended
Reason: Hi! Id like to extend this deadline. Ive been unavailable for a few days due to an illness and Im so far behind! Im feeling MUCH better and looking forward to getting caught up and move with the project. Im not sure how this works, but I attached a list of the oils that we currently have available. And in the list is the idea for the color schemes for the oils. The basic idea is for it to have a wide array of colors, so using different shades of greens, yellows, oranges and so on. So that its like a rainbow. We are not set of that particular color for that particular oil. It was just a idea list of possible colors for oils. Thanks so much!

Target Market(s)

Metro & Modern people. Interested in healthy organic living, Mostly women (some men) 20-45 who are interested in holistic healing.

Industry/Entity Type

It Company

Requirements
Must have
• A reputable look. Clean, organic, crisp, zen or spa-like feel. Modern, youthful appealing label design. Approachable and interesting, not intimidating so that I don't turn away people who are new or not familiar with how to use essential oils.
Should not have
• do NOT want the look to be anywhere close to medicinal, witchy, crafty, hippie, mystical, overly earthy, magical, or voodoo. Do not want it to look like something out of a grandmothers medicine cabinet.

```html
<!DOCTYPE html>
<html lang="en">
<head>
<meta charset="utf-8">
<title>Meadowlark Essentials – Sandalwood Label</title>
<link rel="stylesheet" href="https://fonts.googleapis.com/css2?family=Arimo:wght@400&display=swap">
<style>
  :root {
    --backdrop-light: #f3f5f4;
    --backdrop-dark: #d9dddc;
    --label-top: #e6e7e6;
    --label-band: #3d332b;
    --accent-line: #d9c31b;
    --oil-name: #c8c21f;
    --oil-detail: #a9a44a;
    --brand-ink: #3a3431;
    --wood-light: #a8694a;
    --wood-dark: #6e3f2a;
  }
  html, body {
    margin: 0;
    padding: 0;
    width: 1200px;
    height: 1001px;
    overflow: hidden;
  }
  body {
    background: radial-gradient(ellipse at 60% 40%, var(--backdrop-light) 0%, var(--backdrop-dark) 100%);
    font-family: "Arimo", Arial, sans-serif;
  }
  .label {
    display: block;
    width: 1200px;
    height: 1001px;
  }
  .brand-small { font-size: 26px; letter-spacing: 4px; fill: var(--brand-ink); }
  .brand-large { font-size: 44px; letter-spacing: 2px; fill: var(--brand-ink); }
  .oil-name { font-size: 60px; fill: var(--oil-name); }
  .oil-detail { font-size: 23px; fill: var(--oil-detail); }
</style>
</head>
<body>
<svg class="label" viewBox="0 0 1200 1001" xmlns="http://www.w3.org/2000/svg">
  <defs>
    <clipPath id="label-shape">
      <rect x="110" y="290" width="980" height="420" rx="14"/>
    </clipPath>
    <linearGradient id="wood-tone" x1="0" y1="0" x2="1" y2="1">
      <stop offset="0" stop-color="var(--wood-light)"/>
      <stop offset="0.5" stop-color="var(--wood-dark)"/>
      <stop offset="1" stop-color="var(--wood-light)"/>
    </linearGradient>
  </defs>

  <g clip-path="url(#label-shape)">
    <rect class="label-top" x="110" y="290" width="980" height="132" fill="var(--label-top)"/>
    <rect class="accent-line" x="110" y="422" width="980" height="9" fill="var(--accent-line)"/>
    <rect class="label-band" x="110" y="431" width="980" height="209" fill="var(--label-band)"/>
    <g role="img" aria-label="Photo of sandalwood chips">
      <rect class="wood-strip" x="110" y="640" width="980" height="70" fill="url(#wood-tone)"/>
    </g>
  </g>

  <g class="brand">
    <text class="brand-small" x="600" y="350" text-anchor="middle">MEADOWLARK</text>
    <text class="brand-large" x="600" y="400" text-anchor="middle">ESSENTIALS</text>
  </g>

  <g class="oil-info">
    <text class="oil-name" x="200" y="506">sandalwood</text>
    <text class="oil-detail" x="202" y="548">Santalum Album</text>
    <text class="oil-detail" x="202" y="580">100% Pure Essential Oil</text>
    <text class="oil-detail" x="202" y="612">15 ml</text>
  </g>
</svg>
</body>
</html>
```